Business card

We need a business card design for our company based in Auckland , New Zealand called 'Kestrel + Design Ltd'. We provide architectural services. We would like to see designs that use the max. three colours (such as white, black, grey) The final design should communicate financial safety and growth."
Also I will provide our company logo. I would like to the logo to be embeded onto our business card.

Target Market(s)

new residential house, alteration & addition & light commericila design & drafting service

Industry/Entity Type

Architecture

Contact Information for Business Card

Company name: kestrel + design Ltd.
Name: Mark Telford
Job title: architectural designer & Design RQC
email address: mark@kdstudio.co.nz
mobile number: 02 5319 6620
web site: www.kdstudio.co.nz

Requirements
Must have
• My project must have..
• - embeded logo (attached company logo)
• I don't have a bigger version for our company logo, but I have one old one, so you can remove the word from it)
• - insert the attached small PDGQ logo & RQC logo
• - creative, simple and clear business card.
• - Max. three colours
Nice to have
• - Here are the samples I would like to share with you: http://www.velmorindex.com/blog/minimalistic-business-card-designs/
• I would like to have my business card like one of the creation.
Should not have
• TBA

```html
<!DOCTYPE html>
<html lang="en">
<head>
<meta charset="utf-8">
<title>Kestrel + Design Ltd — Business Card</title>
<link rel="stylesheet" href="https://fonts.googleapis.com/css2?family=Roboto:wght@400;700&display=swap">
<style>
  :root {
    --backdrop: #e8e8e8;
    --card: #3c3c3c;
    --ink: #ffffff;
    --accent: #f2b51c;
    --muted: #d6d6d6;
  }
  * { box-sizing: border-box; margin: 0; padding: 0; }
  html, body {
    width: 1200px;
    height: 960px;
    overflow: hidden;
    background: var(--backdrop);
    font-family: "Roboto", Arial, sans-serif;
  }
  .canvas {
    position: relative;
    width: 1200px;
    height: 960px;
  }
  .card {
    position: absolute;
    top: 335px;
    width: 520px;
    height: 290px;
    background: var(--card);
    box-shadow: 0 10px 24px rgba(0,0,0,0.18);
    overflow: hidden;
  }
  .card--back { left: 60px; }
  .card--front { left: 620px; }

  .badge-seal {
    position: absolute;
    border-radius: 50%;
    background: var(--ink);
  }
  .card--back .badge-seal {
    width: 118px;
    height: 118px;
    left: 201px;
    top: 86px;
  }
  .card--front .badge-seal {
    width: 84px;
    height: 84px;
    left: 44px;
    top: 22px;
  }

  .holder {
    position: absolute;
    left: 28px;
    top: 118px;
  }
  .holder__name {
    color: var(--accent);
    font-weight: 700;
    font-size: 21px;
    letter-spacing: 0.5px;
    line-height: 1.2;
  }
  .holder__title {
    margin-top: 4px;
    color: var(--ink);
    font-size: 11.5px;
    letter-spacing: 0.3px;
  }

  .divider {
    position: absolute;
    left: 22px;
    right: 22px;
    top: 175px;
    height: 1.5px;
    background: var(--ink);
  }

  .membership-badge {
    position: absolute;
    right: 44px;
    top: 112px;
    width: 48px;
    height: 48px;
    background: var(--muted);
  }

  .contacts {
    position: absolute;
    left: 292px;
    top: 190px;
    list-style: none;
  }
  .contacts__item {
    display: flex;
    align-items: center;
    gap: 10px;
    height: 27px;
    color: var(--ink);
    font-size: 11.5px;
    letter-spacing: 0.3px;
  }
  .contacts__icon {
    width: 18px;
    height: 18px;
    flex: none;
  }
</style>
</head>
<body>
<main class="canvas">

  <section class="card card--back" aria-label="Business card, back">
    <div class="badge-seal" role="img" aria-label="Building practitioner certification badge"></div>
  </section>

  <section class="card card--front" aria-label="Business card, front">
    <div class="badge-seal" role="img" aria-label="Building practitioner certification badge"></div>

    <div class="holder">
      <h1 class="holder__name">Mark Telford</h1>
      <p class="holder__title">Architectural Designer &amp; Design RQC</p>
    </div>

    <div class="membership-badge" role="img" aria-label="Professional membership badge"></div>

    <div class="divider"></div>

    <ul class="contacts">
      <li class="contacts__item">
        <svg class="contacts__icon" viewBox="0 0 18 18" aria-hidden="true">
          <circle cx="9" cy="9" r="9" fill="#ffffff"/>
          <rect x="6" y="4" width="6" height="10" rx="1" fill="#3c3c3c"/>
          <rect x="7" y="5.3" width="4" height="6" fill="#ffffff"/>
        </svg>
        <span>02 5319 6620</span>
      </li>
      <li class="contacts__item">
        <svg class="contacts__icon" viewBox="0 0 18 18" aria-hidden="true">
          <circle cx="9" cy="9" r="9" fill="#ffffff"/>
          <rect x="4.5" y="5.5" width="9" height="7" rx="0.8" fill="#3c3c3c"/>
          <path d="M4.8 6 L9 9.4 L13.2 6" fill="none" stroke="#ffffff" stroke-width="1"/>
        </svg>
        <span>mark@kdstudio.co.nz</span>
      </li>
      <li class="contacts__item">
        <svg class="contacts__icon" viewBox="0 0 18 18" aria-hidden="true">
          <circle cx="9" cy="9" r="9" fill="#ffffff"/>
          <g fill="none" stroke="#3c3c3c" stroke-width="1.1">
            <circle cx="9" cy="9" r="4.6"/>
            <ellipse cx="9" cy="9" rx="2" ry="4.6"/>
            <line x1="4.4" y1="9" x2="13.6" y2="9"/>
          </g>
        </svg>
        <span>www.kdstudio.co.nz</span>
      </li>
    </ul>
  </section>

</main>
</body>
</html>
```